Single-sided business card for restaurant bellwether with new logo made on this site

Business card options with new logo including restaurant name, address, phone number and website. This business card is single-sided only and will be presented at the hostess desk for clients to take. I would like to see options based on a cream card background, a white card background, a yellow card background and a burgundy colored background. It needs to be elegant and traditional.

Target Market(s)

local and international crowd

Industry/Entity Type

restaurant

Contact Information for Business Card

address, website and phone number

Font styles to use
Serif

Colors
EE7325
F08F49
F5BC92
FAE3D3
FDF4ED

Requirements
Must have
• new logo, address, phone number, website
Should not have
• more than three colors

```html
<!DOCTYPE html>
<html lang="es">
<head>
<meta charset="utf-8">
<title>Bellwether – Business Card Options</title>
<link href="https://fonts.googleapis.com/css2?family=Crimson+Pro:wght@400;600&display=swap" rel="stylesheet">
<style>
  :root {
    --backdrop: #d6d2cf;
    --orange: #ee7325;
    --orange-soft: #f08f49;
    --ink: #3b1c1c;
    --rule: #c9b8ab;
    --bg-cream: #fdf4ed;
    --bg-white: #ffffff;
    --bg-yellow: #f9e2a6;
    --bg-burgundy: #6b1e2a;
    --ink-light: #fdf4ed;
  }
  * { margin: 0; padding: 0; box-sizing: border-box; }
  html, body {
    width: 1156px; height: 1200px; overflow: hidden;
    background: var(--backdrop);
    font-family: "Crimson Pro", Georgia, serif;
  }
  .card-grid {
    position: absolute; left: 40px; top: 264px;
    display: grid;
    grid-template-columns: 520px 520px;
    grid-auto-rows: 296px;
    gap: 40px 36px;
  }
  .business-card {
    position: relative;
    width: 520px; height: 296px;
    background: var(--card-bg);
    color: var(--card-ink);
    box-shadow: 3px 4px 0 #2a2a2a;
    --card-bg: var(--bg-white);
    --card-ink: var(--ink);
    --card-accent: var(--orange);
    --card-rule: var(--rule);
  }
  .business-card--cream { --card-bg: var(--bg-cream); }
  .business-card--white { --card-bg: var(--bg-white); }
  .business-card--yellow { --card-bg: var(--bg-yellow); --card-rule: #c9a860; }
  .business-card--burgundy {
    --card-bg: var(--bg-burgundy);
    --card-ink: var(--ink-light);
    --card-accent: var(--orange-soft);
    --card-rule: #9a5a63;
  }
  .brand {
    position: absolute; left: 30px; top: 62px; width: 210px;
    display: flex; flex-direction: column; align-items: center;
  }
  .brand-square { width: 96px; height: 96px; background: var(--card-accent); }
  .brand-name {
    margin-top: 18px;
    font-size: 26px; font-weight: 600; letter-spacing: 3px;
    text-transform: uppercase; color: var(--card-ink);
  }
  .accent-rule {
    position: absolute; left: 256px; top: 62px;
    width: 2px; height: 44px; background: var(--card-accent);
  }
  .divider-rule {
    position: absolute; left: 256px; top: 124px;
    width: 1px; height: 120px; background: var(--card-rule);
  }
  .contact { position: absolute; left: 278px; top: 58px; }
  .person-name { font-size: 24px; font-weight: 600; line-height: 1.1; }
  .person-title { font-size: 16px; color: var(--card-accent); margin-top: 3px; }
  .address { margin-top: 22px; font-size: 15px; line-height: 19px; }
  .lines { margin-top: 9px; font-size: 15px; line-height: 19px; }
  .lines b { font-weight: 600; }
</style>
</head>
<body>
  <div class="card-grid">
    <div class="business-card business-card--cream">
      <div class="brand"><div class="brand-square"></div><div class="brand-name">Bellwether</div></div>
      <div class="accent-rule"></div><div class="divider-rule"></div>
      <div class="contact">
        <div class="person-name">Daniel Moreno</div>
        <div class="person-title">General Manager</div>
        <div class="address">Camelia 415<br>Bahías de Tangolunda<br>Oaxaca CP 70989</div>
        <div class="lines"><b>T.</b> 958-555-0142<br><b>E.</b> dan@bellwether.com.mx<br>www.bellwether.com.mx</div>
      </div>
    </div>
    <div class="business-card business-card--white">
      <div class="brand"><div class="brand-square"></div><div class="brand-name">Bellwether</div></div>
      <div class="accent-rule"></div><div class="divider-rule"></div>
      <div class="contact">
        <div class="person-name">Daniel Moreno</div>
        <div class="person-title">General Manager</div>
        <div class="address">Camelia 415<br>Bahías de Tangolunda<br>Oaxaca CP 70989</div>
        <div class="lines"><b>T.</b> 958-555-0142<br><b>E.</b> dan@bellwether.com.mx<br>www.bellwether.com.mx</div>
      </div>
    </div>
    <div class="business-card business-card--yellow">
      <div class="brand"><div class="brand-square"></div><div class="brand-name">Bellwether</div></div>
      <div class="accent-rule"></div><div class="divider-rule"></div>
      <div class="contact">
        <div class="person-name">Daniel Moreno</div>
        <div class="person-title">General Manager</div>
        <div class="address">Camelia 415<br>Bahías de Tangolunda<br>Oaxaca CP 70989</div>
        <div class="lines"><b>T.</b> 958-555-0142<br><b>E.</b> dan@bellwether.com.mx<br>www.bellwether.com.mx</div>
      </div>
    </div>
    <div class="business-card business-card--burgundy">
      <div class="brand"><div class="brand-square"></div><div class="brand-name">Bellwether</div></div>
      <div class="accent-rule"></div><div class="divider-rule"></div>
      <div class="contact">
        <div class="person-name">Daniel Moreno</div>
        <div class="person-title">General Manager</div>
        <div class="address">Camelia 415<br>Bahías de Tangolunda<br>Oaxaca CP 70989</div>
        <div class="lines"><b>T.</b> 958-555-0142<br><b>E.</b> dan@bellwether.com.mx<br>www.bellwether.com.mx</div>
      </div>
    </div>
  </div>
</body>
</html>
```